Fore Sale sign for my real estate agency

I am a Brisbane - Australia inner western suburbs boutique real estate agent who is needing a for sale sign. We are a small dynamic family agency that needs a for sale sign that will standout and give us a strong presence in the market.

I have attached a logo I like, however I am not fixed on anything and am open to suggestions.

The information on the sign should contain but not necessarily limited to the following information - please appreciate I am very open
1 logo - O'Venny
2 Ph number - 3847 1952
3 web address - ovenny.com.au

Thank you
Gareth O'Venny

```html
<!DOCTYPE html>
<html lang="en">
<head>
<meta charset="utf-8">
<title>O'Venny – For Sale Sign</title>
<link href="https://fonts.googleapis.com/css2?family=Open+Sans:wght@700;800&display=swap" rel="stylesheet">
<style>
  :root {
    --backdrop: #f2f2f0;
    --frame: #1e1e1e;
    --sale-red: #c8202a;
    --panel-grey: #e4e4e4;
    --ink: #111111;
    --white: #ffffff;
  }
  * { box-sizing: border-box; margin: 0; padding: 0; }
  html, body {
    width: 1200px;
    height: 1200px;
    overflow: hidden;
    background: var(--backdrop);
  }
  .canvas {
    position: relative;
    width: 1200px;
    height: 1200px;
  }
  .sign {
    position: absolute;
    left: 240px;
    top: 90px;
    width: 720px;
    height: 1020px;
    border: 10px solid var(--frame);
    background: var(--panel-grey);
    font-family: "Open Sans", Arial, sans-serif;
    display: flex;
    flex-direction: column;
  }
  .sign__header {
    height: 250px;
    background: var(--sale-red);
    display: flex;
    align-items: center;
    justify-content: center;
  }
  .sign__headline {
    color: var(--white);
    font-weight: 700;
    font-size: 112px;
    letter-spacing: 1px;
  }
  .sign__body {
    flex: 1;
    display: flex;
    flex-direction: column;
    align-items: center;
    padding-top: 60px;
  }
  .sign__phone {
    color: var(--ink);
    font-weight: 800;
    font-size: 150px;
    letter-spacing: 6px;
    line-height: 1;
  }
  .brand {
    margin-top: 110px;
    display: flex;
    align-items: center;
    gap: 18px;
  }
  .brand__dot {
    width: 96px;
    height: 96px;
    border-radius: 50%;
    background: var(--sale-red);
  }
  .brand__name {
    color: var(--ink);
    font-weight: 700;
    font-size: 112px;
    line-height: 1;
  }
  .brand__domain {
    margin-top: 30px;
    margin-left: 60px;
    color: var(--ink);
    font-weight: 700;
    font-size: 76px;
    line-height: 1;
  }
</style>
</head>
<body>
  <main class="canvas">
    <section class="sign" aria-label="For sale sign">
      <header class="sign__header">
        <h1 class="sign__headline">FOR SALE</h1>
      </header>
      <div class="sign__body">
        <p class="sign__phone">073519</p>
        <div class="brand">
          <span class="brand__dot" aria-hidden="true"></span>
          <span class="brand__name">O'Venny</span>
        </div>
        <p class="brand__domain">.com.au</p>
      </div>
    </section>
  </main>
</body>
</html>
```